Business Card and Letterhead for Juniper Anvil - (Have Logo)

Update 4: Removed company reg no from business card details as it looked a bit out of place. Updated services list.
UPDATE 3
Sorry, I got the address a little bit wrong, have updated it below. Sorry for any inconvenience caused.
UPDATE 2
Finally I have the details for the business cards and letterhead. Submissions already made do not have to be updated unless shortlisted, if all new submissions could include the details for me, Marcus, that would be very much appreciated and help with the final shortlist selection. I intend to share a shortlist of the three best entries with past and existing customers for their feedback and opinions. Thank you all again for your time.
Here are the details.
Marcus Telby
Web Developer
T: 01632 960 418
E: marcus@juniperanvil.example
www.juniperanvil.example
Professional Photography
Web Solutions & E-Commerce
Audio & HD Video Production
Marketing & Promotions
Identity and Branding
Juniper Anvil Ltd
Suite 20938, 3rd Floor
212-224 Orchard Lane
London, N7 9QX
Company Reg. No: 05829147
The order and the layout of the information are of course down to the design, but the company registration number should be smaller and less prominent. The formatting of the telephone and email address using a T: and an E: I am not sure about and again if it is Tel: or Email: or Icons is up to the design.
The Company No. on the letterhead should read (somewhere in small text along the bottom):
Juniper Anvil is a Ltd Company registered in England & Wales, Registration No. 05829147.
The second business card details are
Oliver Brackley
Photographer
T: 01632 960 418
E: oliver@juniperanvil.example
Everything else the same of course.
Thank you again for all the submissions so far.
END OF UPDATE 2
-
UPDATE 1: Please do not alter the logo nor the logo colours. (This was a previous pixel forum project and I am extremely happy with it. The icon can stand alone of course, but I have had to eliminate all entries that have made it black and white, or reversed the icon.) I would like to thank everyone that has participated so far and am very grateful for all your thought and time.
End of Update 1
-
Original Brief:
I have attached the logo vector file.
Following a superb logo from a previous Pixel Forum project I am now looking for a business card design and (although less important) a letterhead as well.
I must admit I tried to do it myself but could only come up with the usual amateur stuff that in comparison to the quality of the logo looked awful.
About Us
Juniper Anvil Ltd will be a new company due to start in January. It is really just me (a web developer) and my friend (a photographer). We will be aiming at the usual small to medium sized businesses in the local area, selling various digital services including photographic services to the public, web hosting and development, commercial photography, modelling services (not us!), full video and film production and possibly a bit of marketing as well. (Really it is anything we can do professionally all lumped together! We met running seperate businesses which have both since closed)
We will not be competing on price. We plan to be expensive but fair. Certainly not the cheapest.
What we are looking for
Business Card
I imagine a double sided business card, which will be used for more than one person. I imagine the front to be the same for everyone and the persons details to be on the back, although this is of course only my thoughts and I am of course completely open to any ideas.
The card could also have a services list or a bit about what we do on it. It might feature the website address, our business address (mail forwarding address) or our registered company number.
Or it might have none of that, we are completely open to any ideas and have no real fixed opinions. I just want it to be really nice :-)
Letterhead (secondary importance)
We will make our decision primarily on the business card, although a mathcing letterhead would be fantastic. Something standardish in format and simple, although again, all ideas are welcomed.
I hope that is enough information but if you have any questions I will answer them as fully and as quickly as possible.
Thank you once again and I really look forward to seeing your ideas and picking a winner.
Marcus T.
Small businesses AND the general public
Film Production

```html
<!DOCTYPE html>
<html lang="en">
<head>
<meta charset="utf-8">
<title>Juniper Anvil – Business Card Concepts</title>
<link rel="stylesheet" href="https://fonts.googleapis.com/css2?family=Archivo+Black&family=Arimo:wght@400;700&display=swap">
<style>
  :root {
    --brand-red: #b50f1f;
    --ink: #231f20;
    --paper: #ffffff;
    --card-edge: #8a8a8a;
    --label-ink: #000000;
  }
  * { margin: 0; padding: 0; box-sizing: border-box; }
  html, body {
    width: 1045px;
    height: 1200px;
    overflow: hidden;
    background: var(--paper);
  }
  .sheet {
    position: relative;
    width: 1045px;
    height: 1200px;
    font-family: "Arimo", Arial, sans-serif;
  }
  .column-label {
    position: absolute;
    top: 0;
    width: 440px;
    text-align: center;
    font-family: "Archivo Black", "Arial Black", sans-serif;
    font-size: 29px;
    letter-spacing: 1px;
    line-height: 38px;
    color: var(--label-ink);
  }
  .column-label--front { left: 2px; }
  .column-label--back { left: 603px; }

  .card {
    position: absolute;
    width: 440px;
    height: 286px;
    background: var(--paper);
    border: 1px solid var(--card-edge);
    overflow: hidden;
  }
  .card--front { left: 2px; }
  .card--back { left: 602px; }
  .row-1 { top: 104px; }
  .row-2 { top: 510px; }
  .row-3 { top: 913px; }

  .band {
    position: absolute;
    left: 0;
    width: 100%;
    background: var(--brand-red);
  }
  .band--top { top: 11px; height: 37px; }
  .band--bottom {
    top: 237px;
    height: 37px;
    display: flex;
    align-items: center;
    justify-content: center;
  }
  .band--wide { top: 50px; height: 187px; }

  .web-address {
    color: var(--paper);
    font-weight: 700;
    font-size: 17px;
    letter-spacing: 0.2px;
  }

  .wordmark {
    position: absolute;
    left: 0;
    top: 124px;
    width: 100%;
    display: flex;
    align-items: center;
    justify-content: center;
    gap: 12px;
  }
  .wordmark__square {
    width: 34px;
    height: 34px;
    background: var(--brand-red);
  }
  .wordmark__name {
    font-weight: 700;
    font-size: 33px;
    line-height: 38px;
    letter-spacing: 0.5px;
    color: var(--ink);
    text-transform: uppercase;
  }
  .wordmark-plate {
    position: absolute;
    left: 53px;
    top: 101px;
    width: 334px;
    height: 86px;
    background: var(--paper);
    display: flex;
    align-items: center;
    justify-content: center;
    gap: 12px;
  }

  .services {
    position: absolute;
    left: 0;
    top: 73px;
    width: 100%;
    list-style: none;
    text-align: center;
    font-size: 23px;
    line-height: 38.5px;
  }
  .services--light { color: var(--paper); }
  .services--red { color: var(--brand-red); }

  .corner {
    position: absolute;
    width: 86px;
    height: 86px;
  }
  .corner svg { display: block; width: 100%; height: 100%; }
  .corner path { fill: var(--brand-red); }
  .corner--top-right { top: 0; right: 0; }
  .corner--top-left { top: 0; left: 0; }
  .corner--bottom-left { bottom: 0; left: 0; }
  .corner--bottom-right { bottom: 0; right: 0; }
</style>
</head>
<body>
<main class="sheet">
  <h2 class="column-label column-label--front">FRONT</h2>
  <h2 class="column-label column-label--back">BACK</h2>

  <!-- Concept 1: bands -->
  <section class="card card--front row-1">
    <div class="band band--top"></div>
    <div class="wordmark">
      <span class="wordmark__square"></span>
      <span class="wordmark__name">Juniper Anvil</span>
    </div>
    <div class="band band--bottom"><span class="web-address">www.juniperanvil.example</span></div>
  </section>
  <section class="card card--back row-1">
    <div class="band band--wide"></div>
    <ul class="services services--light">
      <li>Photography</li>
      <li>Web Hosting &amp; Development</li>
      <li>Commercial Photography</li>
      <li>Video &amp; Film Production</li>
    </ul>
  </section>

  <!-- Concept 2: wide band -->
  <section class="card card--front row-2">
    <div class="band band--wide"></div>
    <div class="wordmark-plate">
      <span class="wordmark__square"></span>
      <span class="wordmark__name">Juniper Anvil</span>
    </div>
  </section>
  <section class="card card--back row-2">
    <div class="band band--top"></div>
    <ul class="services services--red">
      <li>Photography</li>
      <li>Web Hosting &amp; Development</li>
      <li>Commercial Photography</li>
      <li>Video &amp; Film Production</li>
    </ul>
    <div class="band band--bottom"><span class="web-address">www.juniperanvil.example</span></div>
  </section>

  <!-- Concept 3: corners -->
  <section class="card card--front row-3">
    <div class="corner corner--top-right"><svg viewBox="0 0 86 86"><path d="M0 0H86V86Z"/></svg></div>
    <div class="wordmark">
      <span class="wordmark__square"></span>
      <span class="wordmark__name">Juniper Anvil</span>
    </div>
    <div class="corner corner--bottom-left"><svg viewBox="0 0 86 86"><path d="M0 0V86H86Z"/></svg></div>
  </section>
  <section class="card card--back row-3">
    <div class="corner corner--top-left"><svg viewBox="0 0 86 86"><path d="M0 0H86L0 86Z"/></svg></div>
    <ul class="services services--red">
      <li>Photography</li>
      <li>Web Hosting &amp; Development</li>
      <li>Commercial Photography</li>
      <li>Video &amp; Film Production</li>
    </ul>
    <div class="corner corner--bottom-right"><svg viewBox="0 0 86 86"><path d="M86 0V86H0Z"/></svg></div>
  </section>
</main>
</body>
</html>
```